Amber Hollow Gathering - Promotional Poster

Amber Hollow Gathering is a party by the people, for the people. It’s where the grooviest group of creatives comes together to dream, connect, learn and inspire. This incredible forest-stomping celebration is returning in 2023 with our latest event “Lantern Jubilee”
We need your help to create consistent branding that will make the event memorable and recognisable to our attendees. To start with we need a poster announcing the festival theme and our artists for this year.
Here are the key elements we would like you to include in your design:
1. Theme: The branding should reflect the theme of "Lantern Jubilee" with vibrant colours, cosmic imagery, carnival imagery, and celestial elements. It should evoke a sense of wonder, excitement, and adventure.
2. Logo - It should include our Amber Hollow Logo. AI file attached.
3. Text - Amber Hollow (or logo) Presents Lantern Jubilee”
Must haves -
- The logo or festival name
- The Date 5-8th May 2023
- Location - Mudgee NSW
- ticket link www.amberhollowgathering.net
- artist names put in alphabetical order.
Tom Prewitt
Nina Sorrel
Fig jam
Marcus Opley
Vintor
Rhea K
Tova R
Gordon Pim
Ivan morelte
Sandy Fay
Orla P
Tazzo
Fen Tilo
Hugo R & Pell
4. Colour scheme: The colour scheme should be consistent with the theme of "Lantern Jubilee." We would like a range of bold and bright colours that reflect the colours of the cosmos such as purple, blue, and pink.
5. Typography: The typography should be clear and easy to read. We would like a font that reflects the Lantern Jubilee theme.
6. Graphical elements - The poster may include pictorial elements, stars, planets, moons, galaxies, carnival imagery.
7. Marketing collateral: For the winner of this project we need marketing collateral that is consistent with the branding, including artist tiles, posters, banners, social media graphics, and other promotional materials.
8. Deliverables - We need the .Ai .Id or photoshop files at the end of this project.
You can view videos & details of our past events at www.amberhollowgathering.net or on instagram.com/amber_hollow_gathering
We are excited to see your ideas and look forward to working with you

```html
<!DOCTYPE html>
<html lang="en">
<head>
<meta charset="utf-8">
<title>Lantern Jubilee – Amber Hollow Gathering Poster</title>
<link rel="stylesheet" href="https://fonts.googleapis.com/css2?family=Montserrat:wght@400;500;800;900&display=swap">
<style>
  :root {
    --stage: #020338;
    --ink: #ffffff;
    --night: #0a0d45;
    --deep: #141a8a;
    --cobalt: #2a34e0;
    --violet: #6a2be6;
    --magenta: #d050e0;
    --pink: #f2a6f0;
    --aurora: #2ef07a;
    --forest: #0f5a3a;
    --shadow: #080528;
  }
  html, body {
    margin: 0;
    padding: 0;
    width: 1200px;
    height: 833px;
    overflow: hidden;
    background: var(--stage);
  }
  .canvas {
    position: relative;
    width: 1200px;
    height: 833px;
    background: var(--stage);
  }
  .poster {
    position: absolute;
    top: 57px;
    width: 507px;
    height: 720px;
    overflow: hidden;
    color: var(--ink);
    font-family: "Montserrat", sans-serif;
    text-align: center;
  }
  .poster--left { left: 78px; }
  .poster--right { left: 605px; }

  .poster__backdrop {
    position: absolute;
    inset: 0;
    background:
      /* galaxy glow, top right */
      radial-gradient(ellipse 18% 10% at 92% 5%, rgba(242,166,240,0.95), transparent 75%),
      radial-gradient(ellipse 34% 18% at 84% 10%, rgba(208,80,224,0.7), transparent 75%),
      radial-gradient(ellipse 40% 10% at 45% 6%, rgba(120,140,220,0.35), transparent 75%),
      /* aurora, left */
      radial-gradient(ellipse 20% 7% at 14% 37%, rgba(46,240,122,0.95), transparent 75%),
      radial-gradient(ellipse 30% 9% at 30% 40%, rgba(46,240,122,0.6), transparent 75%),
      radial-gradient(ellipse 16% 10% at 8% 48%, rgba(46,240,122,0.55), transparent 75%),
      radial-gradient(ellipse 22% 14% at 14% 60%, rgba(15,90,58,0.9), transparent 75%),
      radial-gradient(ellipse 12% 14% at 34% 72%, rgba(46,240,122,0.45), transparent 75%),
      /* carnival mask light, right */
      radial-gradient(ellipse 26% 22% at 86% 56%, rgba(208,80,224,0.75), transparent 75%),
      radial-gradient(ellipse 20% 18% at 92% 34%, rgba(180,40,120,0.6), transparent 75%),
      /* central purple beam */
      radial-gradient(ellipse 30% 48% at 55% 48%, rgba(140,70,255,0.8), transparent 75%),
      /* crowd shadow, bottom */
      linear-gradient(180deg, transparent 70%, rgba(8,5,40,0.65) 82%, rgba(8,5,40,0.95) 100%),
      linear-gradient(180deg, var(--night) 0%, var(--deep) 18%, var(--cobalt) 42%, var(--violet) 66%, #3a1aa8 80%, var(--shadow) 100%);
  }
  .poster__content {
    position: absolute;
    inset: 0;
  }
  .presents {
    position: absolute;
    top: 64px;
    left: 0;
    right: 0;
    margin: 0;
    font-size: 12.5px;
    font-weight: 400;
    letter-spacing: 3px;
  }
  .title {
    position: absolute;
    top: 92px;
    left: 0;
    right: 0;
    margin: 0;
    font-weight: 400;
  }
  .title__main {
    display: block;
    font-size: 60px;
    line-height: 1;
    letter-spacing: 6px;
  }
  .title__sub {
    display: block;
    margin-top: 18px;
    font-size: 25px;
    font-weight: 500;
    line-height: 1;
    letter-spacing: 11px;
  }
  .lineup {
    position: absolute;
    top: 226px;
    left: 0;
    right: 0;
  }
  .lineup__heading {
    margin: 0 0 10px;
    font-size: 12.5px;
    font-weight: 500;
    letter-spacing: 3px;
  }
  .lineup__list {
    list-style: none;
    margin: 0;
    padding: 0;
  }
  .lineup__list li {
    font-size: 12.5px;
    font-weight: 900;
    line-height: 18.5px;
    letter-spacing: 2.6px;
    text-transform: uppercase;
  }
  .lineup__rule {
    width: 89px;
    height: 2px;
    margin: 7px auto 0;
    background: var(--ink);
    border: 0;
  }
  .details {
    position: absolute;
    top: 539px;
    left: 0;
    right: 0;
    margin: 0;
    font-size: 12px;
    font-weight: 500;
    line-height: 18px;
    letter-spacing: 2.6px;
  }
  .brand {
    position: absolute;
    top: 668px;
    left: 0;
    right: 0;
    margin: 0;
    display: flex;
    align-items: center;
    justify-content: center;
    gap: 8px;
    font-size: 10.5px;
    font-weight: 400;
    letter-spacing: 3.5px;
  }
  .brand__mark {
    width: 7px;
    height: 7px;
    border: 1px solid var(--ink);
    border-radius: 50%;
  }
  .ticket-link {
    position: absolute;
    top: 690px;
    left: 0;
    right: 0;
    margin: 0;
    font-size: 9.5px;
    font-weight: 500;
    letter-spacing: 2px;
  }
</style>
</head>
<body>
<main class="canvas">

  <article class="poster poster--left">
    <div class="poster__backdrop" role="img" aria-label="Starry night sky with a pink galaxy, green aurora over forest treetops, a carnival mask in purple light and a festival crowd in silhouette"></div>
    <div class="poster__content">
      <p class="presents">AMBER HOLLOW &nbsp;PRESENTS</p>
      <h1 class="title">
        <span class="title__main">LANTERN</span>
        <span class="title__sub">JUBILEE</span>
      </h1>
      <section class="lineup">
        <h2 class="lineup__heading">ARTISTS</h2>
        <ul class="lineup__list">
          <li>Fen Tilo</li>
          <li>Fig jam</li>
          <li>Gordon Pim</li>
          <li>Hugo R &amp; Pell</li>
          <li>Ivan morelte</li>
          <li>Marcus Opley</li>
          <li>Nina Sorrel</li>
          <li>Orla P</li>
          <li>Rhea K</li>
          <li>Sandy Fay</li>
          <li>Tazzo</li>
          <li>Tom Prewitt</li>
          <li>Tova R</li>
          <li>Vintor</li>
        </ul>
        <hr class="lineup__rule">
      </section>
      <p class="details">5-8TH MAY 2023<br>MUDGEE NSW</p>
      <p class="brand"><span class="brand__mark"></span>AMBER HOLLOW GATHERING</p>
      <p class="ticket-link">www.amberhollowgathering.net</p>
    </div>
  </article>

  <article class="poster poster--right">
    <div class="poster__backdrop" role="img" aria-label="Starry night sky with a pink galaxy, green aurora over forest treetops, a carnival mask in purple light and a festival crowd in silhouette"></div>
    <div class="poster__content">
      <p class="presents">AMBER HOLLOW &nbsp;PRESENTS</p>
      <h1 class="title">
        <span class="title__main">LANTERN</span>
        <span class="title__sub">JUBILEE</span>
      </h1>
      <section class="lineup">
        <h2 class="lineup__heading">ARTISTS</h2>
        <ul class="lineup__list">
          <li>Fen Tilo</li>
          <li>Fig jam</li>
          <li>Gordon Pim</li>
          <li>Hugo R &amp; Pell</li>
          <li>Ivan morelte</li>
          <li>Marcus Opley</li>
          <li>Nina Sorrel</li>
          <li>Orla P</li>
          <li>Rhea K</li>
          <li>Sandy Fay</li>
          <li>Tazzo</li>
          <li>Tom Prewitt</li>
          <li>Tova R</li>
          <li>Vintor</li>
        </ul>
        <hr class="lineup__rule">
      </section>
      <p class="details">5-8TH MAY 2023<br>MUDGEE NSW</p>
      <p class="brand"><span class="brand__mark"></span>AMBER HOLLOW GATHERING</p>
      <p class="ticket-link">www.amberhollowgathering.net</p>
    </div>
  </article>

</main>
</body>
</html>
```